We need a design for our website called Mivelda which is a brazilian e-commerce focused on childrenswear. Basically your are able to swap (sell & buy) your kids outgrown clothes in the website and we will offer all the necessary services to help you on that.

We believe the main characteristic of the company is the swap of clothes and accessories, but we also feel that by doing this we are guaranteeing that this clothes are not going to trash, reducing clothes waste and being friendly with the environment.

We believe it should be clean with solid and soft colors (refer to the logo attached) and should communicate high quality standards and trust.

We need 2 web pages: home/search results and product details. In both pages we would like to have a fixed top bar with the logo, menu (Buy, Sell, About Us), login, a short message and shopping cart. As well as a footer on the botton with different options and social network links.

- Home/search results: right at the beginning of the page we would like to have a welcome/explanatory carousel banner. It should be a conventional 2 columns design with filters on the left (~25%) and the results on the main section (~3/4 products per row). We need filters for clothes and accessories (size,category, brands, color, gender).

- Product details: again, this should be very clean, with breadcrumbs on the top, a very short description (product's name, category, size), price, "Add to cart" button, an image with zoom functionality (as reference: jquery jqzoom), a "Similar Items" box and a share bar (chatloom, quibbly, snapquilt, v+).

Please bear in mind that we plan to use the main template in different colors across the website.
Updates

Hi everyone! 

We have just updated the brief to add some "Must have features" and "Nice to have features". Please take a careful look at it as it affects pretty much every design we received so far.

We will guarantee the project in the next 1-2 days, but we first would like to see some initial proposals for the second page (product details). Some of you guys are doing an awesome job in the home page!

Best,

Mivelda team

We have just updated the contest payment status: it is now committed!

Best,
Mivelda Team

Target Market(s)

The main audience will be parents of any age

Industry/Entity Type

E-Commerce

Requirements
Must have
• We would like to have only the following elements in the header: logo, login, cart image, Home, "Compre" (Buy), "Venda" (Sell) - not necessarily in this order
- The header should be persistent all over the website (always fixed at the top), thus, if it is too thick it will end up eating too much vertical space in some pages
- The current page should be somehow highlited in the header
- Right next to the cart image on the top we need a small tag indicating how many itens are already inside the cart
- We need a button "Entenda como funcionamos" (which in english means "Learn more") in the banner
- Please use an image of childrens in the banner (not clothes or teenagers)
- Besides the banner, the user in a1024x768 screen resolution should at least be able to view the first row of search results
- There is no need for a "Add to cart" button in every search result (keep price, size, type only). This option should only be available in the second page (product details)
- When needed use "Adicionar ao carrinho" (portuguese) instead of "Add to cart" (english)
- Regarding social network links in the footer, we only need chatloom, quibbly, snapquilt, v+
- In the search results page we need an option to show 12, 24, 48 results per page
- Users need to be able to sort the results (newest first, price low-high and high-low)
Nice to have
• We don´t need a text search box anywhere in the website
- There is no need to present the payment methods in neither pages
- The image of the cart should be modified when there are items inside (full vs empty)
- When the user moves the mouse over the cart image, a simple "div" should show up bellow it listing all items
- Regarding social network links, we like icons that change colors when the user
moves the mouse over them
- Regarding the color scheme, use up to a max of 3 colors and feel free to change the logo colors if you find a better combination than the ones we provided

```html
<!DOCTYPE html>
<html lang="pt-BR">
<head>
<meta charset="utf-8">
<title>Mivelda – Sell, buy or swap kids clothes</title>
<link href="https://fonts.googleapis.com/css2?family=Dosis:wght@400;500;600;700&display=swap" rel="stylesheet">
<style>
:root{
  --purple:#8783c9;
  --purple-dark:#6e6ab3;
  --green:#3cb878;
  --orange:#f2a160;
  --orange-dark:#e08a44;
  --red:#e63c3f;
  --ink:#3a3a3a;
  --muted:#6f6f6f;
  --line:#dedede;
  --panel:#f1f1f1;
  --page:#ececec;
  --white:#ffffff;
}
*{box-sizing:border-box;margin:0;padding:0}
html,body{width:730px;height:1200px;overflow:hidden}
body{background:var(--page);font-family:"Dosis",sans-serif;color:var(--ink);position:relative;font-size:10px}

/* header + banner card */
.hero-card{position:absolute;left:74px;top:0;width:584px;height:246px;background:var(--white);border:1px solid #dcdcdc;border-top:none;border-radius:0 0 6px 6px;box-shadow:0 1px 3px rgba(0,0,0,.08)}
.ribbon-tail{position:absolute;top:28px}
.nav-band{position:absolute;left:265px;top:21px;width:393px;height:31px;background:var(--purple);z-index:2}
.main-nav{position:absolute;left:278px;top:28px;display:flex;gap:14px;color:var(--white);font-size:13px;font-weight:500;z-index:3}
.logo-box{position:absolute;left:87px;top:11px;width:178px;height:58px;background:var(--white);box-shadow:0 2px 5px rgba(0,0,0,.18);display:flex;align-items:center;justify-content:center;z-index:3}
.logo-name{font-size:34px;font-weight:500;color:var(--green);letter-spacing:.5px}
.account-links{position:absolute;left:545px;top:4px;font-size:9px;color:var(--purple-dark)}
.account-links span{margin:0 4px;color:#999}
.cart-summary{position:absolute;left:544px;top:27px;width:80px;height:18px;background:#f3f3f3;border:1px solid #ddd;border-radius:3px;display:flex;align-items:center;font-size:10px;color:#666;z-index:6}
.cart-summary b{font-weight:500;padding:0 5px;border-right:1px solid #ccc}
.cart-summary i{font-style:normal;padding-left:5px}
.cart-badge{position:absolute;left:619px;top:16px;width:38px;height:38px;border-radius:50%;background:var(--white);box-shadow:0 1px 3px rgba(0,0,0,.25);display:flex;align-items:center;justify-content:center;z-index:7}
.cart-drop{position:absolute;left:544px;top:46px;width:108px;height:96px;background:var(--white);border:1px solid #ddd;box-shadow:0 2px 5px rgba(0,0,0,.25);padding:5px 5px;z-index:6}
.drop-item{display:flex;align-items:center;height:27px;border-bottom:1px solid #eee;margin-bottom:3px}
.drop-thumb{width:14px;height:18px;border-radius:2px;margin-right:6px;flex:none}
.drop-name{font-size:9px;font-weight:700;line-height:1}
.drop-name small{display:block;font-size:7px;font-weight:400;color:#888;margin-top:1px}
.drop-price{margin-left:auto;font-size:10px;font-weight:600}
.drop-foot{display:flex;align-items:center;margin-top:10px;font-size:9px;font-weight:600;white-space:nowrap}
.btn-checkout{background:var(--orange);color:var(--white);font-size:8px;padding:3px 4px;border-radius:2px;margin-right:5px}
.drop-foot em{font-style:normal;color:var(--red)}

.banner-title{position:absolute;left:98px;top:83px;font-size:20px;line-height:26px;font-weight:700;color:#5a5a5a;letter-spacing:.1px;white-space:nowrap;z-index:2}
.banner-copy{position:absolute;left:98px;top:146px;width:240px;font-size:12.5px;line-height:15px;color:#555}
.btn-primary{position:absolute;left:97px;top:202px;width:104px;height:27px;background:var(--orange);border-radius:3px;color:var(--white);font-size:12px;font-weight:500;display:flex;align-items:center;justify-content:center;box-shadow:inset 0 -2px 0 var(--orange-dark)}
.kids-photo{position:absolute;left:390px;top:54px;width:250px;height:191px;border-radius:4px;background:linear-gradient(90deg,#f3e37a 0%,#f4b36f 22%,#d9534f 42%,#5a6a8f 60%,#e8a0a8 78%,#dfe4ea 100%);opacity:.85;z-index:1}
.slide-prev{position:absolute;left:74px;top:135px;width:14px;height:20px;background:#d9d9d9;display:flex;align-items:center;justify-content:center}
.slide-next{position:absolute;left:642px;top:145px;width:16px;height:16px;background:var(--purple);display:flex;align-items:center;justify-content:center;z-index:2}

/* sidebar */
.sidebar{position:absolute;left:73px;top:266px;width:141px;height:660px;background:var(--white);box-shadow:0 1px 3px rgba(0,0,0,.12)}
.box-head{height:27px;background:var(--purple);color:var(--white);font-size:13px;font-weight:600;display:flex;align-items:center;padding-left:8px;gap:7px}
.bar{position:absolute;left:0;width:141px;height:24px;background:var(--panel);border-top:1px solid #e2e2e2;border-bottom:1px solid #e2e2e2;display:flex;align-items:center;padding:0 6px;font-size:12px;color:#555;gap:6px}
.bar::after{content:"";margin-left:auto;border-left:5px solid #666;border-top:4px solid transparent;border-bottom:4px solid transparent}
.checks{position:absolute;left:6px;font-size:8.5px;color:#444;line-height:13px}
.checks li{list-style:none;display:flex;align-items:center;gap:4px}
.box{width:7px;height:7px;border:1px solid #aaa;display:inline-block;position:relative;background:#fff}
.box.on::after{content:"";position:absolute;left:1px;top:0;width:2px;height:4px;border:solid var(--green);border-width:0 1.5px 1.5px 0;transform:rotate(45deg)}
.btn-small{position:absolute;background:linear-gradient(#f7f7f7,#dcdcdc);border:1px solid #b9b9b9;border-radius:2px;font-size:7.5px;font-weight:600;color:#444;display:flex;align-items:center;justify-content:center}
.gender{position:absolute;left:4px;top:155px;font-size:11px;color:#555;display:flex;align-items:center;gap:6px}
.gender em{font-size:10px;color:#666;display:flex;align-items:center;gap:3px}
.cat-list{position:absolute;left:8px;top:214px;font-size:10px;line-height:17px;color:#444;list-style:none}
.cat-list li::before{content:"›";color:#999;margin-right:5px}
.cat-list .current{color:var(--purple-dark);text-decoration:underline}
.sizes{position:absolute;left:5px;top:313px;width:135px;display:flex;flex-wrap:wrap;gap:5px 4px}
.sizes span{width:22px;height:13px;border:1px solid #ccc;font-size:8px;display:flex;align-items:center;justify-content:center;color:#555}
.sizes .on{background:var(--orange);border-color:var(--orange-dark);color:var(--white)}
.brand-search{position:absolute;left:6px;top:485px;width:124px;height:16px;border:1px solid #ccc;font-size:8px;font-style:italic;color:#777;padding-left:4px;display:flex;align-items:center}
.brand-search svg{margin-left:auto;margin-right:3px}
.colors{position:absolute;left:6px;top:592px;display:flex;gap:1px}
.colors span{width:9px;height:9px}
.advance{position:absolute;left:9px;top:642px;font-size:8px;font-style:italic;color:var(--purple-dark)}

.subscribe{position:absolute;left:73px;top:938px;width:141px;height:112px;background:var(--white);box-shadow:0 1px 3px rgba(0,0,0,.12)}
.subscribe p{position:absolute;left:6px;top:36px;font-size:8.5px;line-height:11px;color:#444}
.field{position:absolute;left:6px;top:65px;width:126px;height:17px;border:1px solid #ccc;font-size:8px;font-style:italic;color:#999;padding-left:4px;display:flex;align-items:center}

/* results */
.toolbar{position:absolute;left:227px;top:265px;width:430px;height:16px;font-size:9px;color:#555;display:flex;align-items:center}
.pill{border:1px solid #ddd;background:#fff;padding:1px 6px;margin:0 6px 0 4px;font-style:italic;font-size:9px}
.per-page{margin-left:auto;display:flex;align-items:center;gap:4px}
.select{width:34px;height:15px;border:1px solid #ccc;background:#fff;display:flex;align-items:center;padding-left:4px;position:relative}
.select::after{content:"";position:absolute;right:3px;top:5px;border-top:4px solid #666;border-left:3px solid transparent;border-right:3px solid transparent}

.grid{position:absolute;left:227px;top:297px;display:grid;grid-template-columns:repeat(4,98px);column-gap:13px;row-gap:17px}
.card{position:relative;height:161px;background:var(--white);box-shadow:0 1px 3px rgba(0,0,0,.18);overflow:hidden}
.card.active{outline:1.5px solid var(--green)}
.shot{position:absolute;left:14px;top:8px;width:70px;height:82px;border-radius:6px}
.overlay{position:absolute;left:0;top:60px;width:98px;height:36px;background:rgba(40,40,40,.85);display:flex;align-items:center;justify-content:center;gap:8px}
.rule{position:absolute;left:6px;right:6px;top:103px;border-top:1px solid #e5e5e5}
.name{position:absolute;left:6px;top:107px;font-size:9px;font-weight:600;color:#333}
.size{position:absolute;left:6px;top:120px;font-size:7.5px;color:#555}
.price{position:absolute;right:8px;top:138px;font-size:12px;font-weight:600;color:var(--red)}
.old{position:absolute;left:6px;top:139px;font-size:10.5px;color:#999;text-decoration:line-through}
.sale{position:absolute;right:-1px;top:136px;height:17px;padding:0 6px 0 9px;background:var(--orange);color:var(--white);font-size:11.5px;font-weight:600;display:flex;align-items:center;clip-path:polygon(6px 0,100% 0,100% 100%,6px 100%,0 50%)}
.new-tag{position:absolute;left:-17px;top:9px;width:64px;height:13px;background:var(--green);color:var(--white);font-size:8px;font-weight:700;text-align:center;line-height:13px;transform:rotate(-45deg)}
.deal-tag{position:absolute;left:4px;top:4px;width:12px;height:9px;background:#a6a3d8;border-radius:2px;transform:rotate(-35deg)}

.pager{position:absolute;left:530px;top:1009px;display:flex;gap:4px;font-size:8.5px;color:#444}
.pager span{min-width:15px;height:15px;border:1px solid #ccc;background:#f6f6f6;display:flex;align-items:center;justify-content:center;border-radius:2px}
.pager .on{background:#e2e2e2;border-color:#999}
.pager .gap{border:none;background:none;min-width:6px}

/* footer */
.site-footer{position:absolute;left:0;top:1063px;width:730px;height:108px;background:linear-gradient(#e2e2e2,#e9e9e9)}
.foot-title{position:absolute;font-size:10.5px;font-weight:600;color:#555}
.foot-links{position:absolute;top:1095px;list-style:none;font-size:8.5px;line-height:14.6px;color:#444}
.foot-links li::before{content:"•";color:#888;margin-right:4px}
.socials{position:absolute;left:338px;top:1098px;display:grid;grid-template-columns:repeat(2,56px);row-gap:5px;font-size:9px;color:#444}
.socials span{display:flex;align-items:center;gap:4px}
.socials i{width:11px;height:11px;background:#555}
.contact{position:absolute;left:517px;top:1092px;font-size:8.5px;line-height:14px;color:#444}
.contact div{display:flex;align-items:center;gap:7px}
.contact address{font-style:normal;margin-top:4px}
.footer-rule{position:absolute;left:74px;top:1171px;width:584px;border-top:1px solid #d0d0d0}
.copyright{position:absolute;left:0;top:1177px;width:730px;text-align:center;font-size:8.5px;color:#555}
</style>
</head>
<body>

<!-- header -->
<svg class="ribbon-tail" style="left:20px" width="56" height="30" viewBox="0 0 56 30" aria-hidden="true"><path d="M0 2 H54 V28 H0 L9 15 Z" fill="#7c78c0"/><path d="M46 -6 L54 2 H46 Z" fill="#5a5697"/></svg>
<svg class="ribbon-tail" style="left:656px" width="56" height="30" viewBox="0 0 56 30" aria-hidden="true"><path d="M2 2 H56 L47 15 L56 28 H2 Z" fill="#7c78c0"/></svg>
<div class="hero-card"></div>
<div class="kids-photo" role="img" aria-label="Photo of five smiling children with school backpacks standing in a row"></div>
<div class="nav-band"></div>
<nav class="main-nav"><span>Compre</span><span>Venda</span><span>Como Funciona</span></nav>
<div class="logo-box"><span class="logo-name">Mivelda</span></div>
<div class="account-links">Login<span>|</span>Sign Up</div>
<div class="cart-summary"><b>$8.90</b><i>2 artigo</i></div>
<div class="cart-badge">
  <svg width="26" height="22" viewBox="0 0 26 22" aria-label="Carrinho"><path d="M7 8 L13 2 L19 8" fill="none" stroke="#b8892e" stroke-width="1.6"/><rect x="4" y="6" width="18" height="4" rx="1" fill="#f0c24a"/><path d="M2 9 H24 L21 20 H5 Z" fill="#e3393c"/><path d="M7 12 V18 M11 12 V18 M15 12 V18 M19 12 V18" stroke="#fff" stroke-width="1.2"/></svg>
</div>
<div class="cart-drop">
  <div class="drop-item"><span class="drop-thumb" role="img" aria-label="Striped dress thumbnail" style="background:linear-gradient(#e46a7a,#f3c2c8)"></span><span class="drop-name">DRESS<small>Quantati: 1</small></span><span class="drop-price">$ 4,95</span></div>
  <div class="drop-item"><span class="drop-thumb" role="img" aria-label="Cap thumbnail" style="background:#2f3d5e"></span><span class="drop-name">CAP<small>Quantati: 1</small></span><span class="drop-price">$ 3,95</span></div>
  <div class="drop-foot"><span class="btn-checkout">CHECKOUT</span>TOTAL :&nbsp;<em>$ 8.90</em></div>
</div>

<!-- banner -->
<h1 class="banner-title">SELL AND BUY OR SWAP<br>YOUR KIDS OUTGROWN CLOTHES</h1>
<p class="banner-copy">Curabitur aliquam magna ac quam mollis placerat. Sed varius neque quis nunc ullamcorper consecte tur condimentum ipsum venenatis.</p>
<div class="btn-primary">COMO FUNCIONA</div>
<div class="slide-prev"><svg width="6" height="8" aria-hidden="true"><path d="M5 0 L0 4 L5 8 Z" fill="#888"/></svg></div>
<div class="slide-next"><svg width="6" height="8" aria-hidden="true"><path d="M1 0 L6 4 L1 8 Z" fill="#fff"/></svg></div>

<!-- sidebar filters -->
<aside class="sidebar">
  <div class="box-head"><svg width="12" height="12" aria-hidden="true"><circle cx="5" cy="5" r="3.6" fill="none" stroke="#fff" stroke-width="1.6"/><path d="M8 8 L11 11" stroke="#fff" stroke-width="1.8"/></svg>FILTER BY</div>
  <div class="bar" style="top:29px"><svg width="10" height="7" aria-hidden="true"><ellipse cx="5" cy="3.5" rx="5" ry="3.2" fill="#666"/><circle cx="5" cy="3.5" r="1.4" fill="#fff"/></svg>Active Filter</div>
  <ul class="checks" style="top:60px">
    <li><i class="box on"></i>Price range:&nbsp; $ 20 &nbsp;•&nbsp; $ 40</li>
    <li><i class="box on"></i>Size:&nbsp;&nbsp;&nbsp;&nbsp;&nbsp;&nbsp;&nbsp;&nbsp; 6m - 1 y</li>
    <li><i class="box on"></i>Color:&nbsp;&nbsp;&nbsp;&nbsp;&nbsp;&nbsp; <span style="width:9px;height:9px;background:#19a8e8;display:inline-block"></span></li>
    <li><i class="box on"></i>Color:&nbsp;&nbsp;&nbsp;&nbsp;&nbsp;&nbsp; K&amp;L</li>
  </ul>
  <div class="btn-small" style="left:6px;top:125px;width:52px;height:16px">CLEAR FILTER</div>
  <div class="gender">Gender <em><i class="box on"></i>Boy</em><em><i class="box"></i>Girl</em></div>
  <div class="bar" style="top:180px"><svg width="10" height="8" aria-hidden="true"><path d="M0 2 L3 0 H7 L10 2 L9 4 H8 V8 H2 V4 H1 Z" fill="#666"/></svg>Categories</div>
  <ul class="cat-list"><li class="current">T-Shirts</li><li>Dress</li><li>Pants</li></ul>
  <div class="bar" style="top:272px"><svg width="10" height="10" aria-hidden="true"><path d="M1 9 L9 1" stroke="#666" stroke-width="3"/></svg>Tamanho</div>
  <div class="sizes"><span>6 m</span><span>1y</span><span class="on">3y</span><span>6y</span><span>7y</span><span>8y</span><span>10y</span></div>
  <div class="bar" style="top:356px"><svg width="10" height="10" aria-hidden="true"><path d="M1 5 L5 1 H9 V5 L5 9 Z" fill="none" stroke="#666" stroke-width="1.4"/></svg>Price</div>
  <ul class="checks" style="top:386px;line-height:11px">
    <li><i class="box on"></i>$ 20 &nbsp;•&nbsp; $ 40</li>
    <li><i class="box"></i>$ 40 &nbsp;•&nbsp; $ 60</li>
    <li><i class="box"></i>$ 60 &nbsp;•&nbsp; $ 80</li>
    <li><i class="box"></i>$ 80 &nbsp;•&nbsp; $ 100</li>
    <li><i class="box"></i>$ 100 &nbsp;•&nbsp; $ 120</li>
  </ul>
  <div class="bar" style="top:451px"><svg width="10" height="10" aria-hidden="true"><circle cx="5" cy="5" r="4.5" fill="#666"/></svg>Marca</div>
  <div class="brand-search">Adora<svg width="10" height="10" aria-hidden="true"><circle cx="4" cy="4" r="3" fill="none" stroke="#666" stroke-width="1.3"/><path d="M6 6 L9 9" stroke="#666" stroke-width="1.5"/></svg></div>
  <ul class="checks" style="top:506px;line-height:11px">
    <li><i class="box on"></i>K&amp;L</li>
    <li><i class="box"></i>Adora</li>
    <li><i class="box"></i>Venbelo</li>
    <li><i class="box"></i>R&amp;R</li>
  </ul>
  <div class="bar" style="top:556px;padding-left:16px">Cor</div>
  <div class="colors"><span style="background:#111"></span><span style="background:#8a8a8a"></span><span style="background:#e62222"></span><span style="background:#1aa3e8"></span><span style="background:#3e9e3a"></span><span style="background:#2d9d6a"></span><span style="background:#6a1f8a"></span><span style="background:#1e5fb0"></span><span style="background:#0e7f8f"></span><span style="background:#e66b1d"></span><span style="background:#8a5a2a"></span><span style="background:#8e5ec2"></span></div>
  <div class="btn-small" style="left:7px;top:619px;width:50px;height:17px;font-size:9px">FILTER</div>
  <div class="advance">Advance Search &nbsp;→</div>
</aside>

<section class="subscribe">
  <div class="box-head"><svg width="12" height="9" aria-hidden="true"><rect width="12" height="9" fill="#fff"/><path d="M0 0 L6 5 L12 0" fill="none" stroke="#8783c9" stroke-width="1.2"/></svg>SUBSCRIBE</div>
  <p>Get the atest updates with<br>our Newsletter</p>
  <div class="field">Your email address</div>
  <div class="btn-small" style="left:6px;top:89px;width:46px;height:14px">SUBMIT</div>
</section>

<!-- results -->
<div class="toolbar">Resultados:<span class="pill">latest</span>Preço<span class="pill">low price</span><span class="per-page">Resultados por página <span class="select">12</span></span></div>

<main class="grid">
  <article class="card"><div class="shot" role="img" aria-label="Navy polka-dot dress" style="background:#2b3452"></div><span class="new-tag">NOVO</span><i class="rule"></i><h3 class="name">DRESS</h3><p class="size">SIZE: 1½-2Y - 6-8Y</p><s class="old">R$ 20,95</s><span class="sale">R$ 17,95</span></article>
  <article class="card active"><div class="shot" role="img" aria-label="Pink and white striped dress" style="background:linear-gradient(#e25a6d,#f6c7cf)"></div><div class="overlay"><svg width="20" height="14" aria-label="Adicionar ao carrinho"><path d="M1 4 H19 L17 13 H3 Z M5 4 L10 0 L15 4" fill="none" stroke="#fff" stroke-width="1.3"/></svg><svg width="18" height="17" aria-label="Favorito"><path d="M9 0 L11.6 5.6 L18 6.3 L13.2 10.6 L14.6 17 L9 13.7 L3.4 17 L4.8 10.6 L0 6.3 L6.4 5.6 Z" fill="#b8b8b8"/></svg></div><i class="rule"></i><h3 class="name">DRESS</h3><p class="size">SIZE: 1½-2Y - 6-8Y</p><span class="price">$ 4,95</span></article>
  <article class="card"><div class="shot" role="img" aria-label="Pink tulle skirt" style="background:#f5a7c2"></div><i class="deal-tag"></i><i class="rule"></i><h3 class="name">TULLE SKIRT</h3><p class="size">SIZE: 1½-2Y - 7-8Y</p><span class="price">R$ 14,95</span></article>
  <article class="card"><div class="shot" role="img" aria-label="Denim skirt" style="background:#3e4f6e"></div><i class="rule"></i><h3 class="name">JEANS SKIRT</h3><p class="size">SIZE: 1½-2Y - 7-8Y</p><span class="price">R$ 14,95</span></article>

  <article class="card"><div class="shot" role="img" aria-label="Blue hooded jacket" style="background:#2f5aa8"></div><i class="deal-tag"></i><i class="rule"></i><h3 class="name">JACKET</h3><p class="size">SIZE: 1½-2Y - 6-8Y</p><span class="price">R$ 22,95</span></article>
  <article class="card"><div class="shot" role="img" aria-label="Dark denim jeans" style="background:#2e3d5c"></div><i class="rule"></i><h3 class="name">JEANS</h3><p class="size">SIZE: 1½-2Y - 6-8Y</p><span class="price">R$ 10,95</span></article>
  <article class="card"><div class="shot" role="img" aria-label="Navy knit cap with cartoon print" style="background:#2a3a5c"></div><span class="new-tag">NOVO</span><i class="rule"></i><h3 class="name">CAP</h3><p class="size">SIZE: 1½-2Y - 7-8Y</p><span class="price">R$ 3,95</span></article>
  <article class="card"><div class="shot" role="img" aria-label="Three pairs of gloves in navy, stripes and teal" style="background:linear-gradient(90deg,#2b3550,#d77a6a,#3fc3c0)"></div><i class="rule"></i><h3 class="name">3 PACK GOVES</h3><p class="size">SIZE: 1½-2Y - 7-8Y</p><span class="price">R$ 7,95</span></article>

  <article class="card"><div class="shot" role="img" aria-label="Royal blue printed t-shirt" style="background:#2c56c8"></div><i class="rule"></i><h3 class="name">T-SHIRT</h3><p class="size">SIZE: 1½-2Y - 6-8Y</p><span class="price">R$ 5,95</span></article>
  <article class="card active"><div class="shot" role="img" aria-label="Blue and white striped t-shirt" style="background:linear-gradient(#4a7fb0,#dbe6f0)"></div><div class="overlay"><svg width="20" height="14" aria-label="Adicionar ao carrinho"><path d="M1 4 H19 L17 13 H3 Z M5 4 L10 0 L15 4" fill="none" stroke="#e63c3f" stroke-width="1.3"/></svg><svg width="18" height="17" aria-label="Favorito"><path d="M9 0 L11.6 5.6 L18 6.3 L13.2 10.6 L14.6 17 L9 13.7 L3.4 17 L4.8 10.6 L0 6.3 L6.4 5.6 Z" fill="#f5b82e"/></svg></div><i class="rule"></i><h3 class="name">T-SHIRT</h3><p class="size">SIZE: 1½-2Y - 6-8Y</p><span class="price">R$ 5,95</span></article>
  <article class="card"><div class="shot" role="img" aria-label="Grey hooded sweater" style="background:#b2b2b2"></div><i class="rule"></i><h3 class="name">HOODED SWEATER</h3><p class="size">SIZE: 1½-2Y - 7-8Y</p><s class="old">R$ 20,95</s><span class="sale">R$ 17,95</span></article>
  <article class="card"><div class="shot" role="img" aria-label="Mint green polo shirt" style="background:#6fdcc2"></div><i class="deal-tag"></i><i class="rule"></i><h3 class="name">SUMMER SHIRT</h3><p class="size">SIZE: 1½-2Y - 7-8Y</p><span class="price">R$ 7,95</span></article>

  <article class="card"><div class="shot" role="img" aria-label="Denim skirt" style="background:#3e4f6e"></div><i class="rule"></i><h3 class="name">JEANS SKIRT</h3><p class="size">SIZE: 1½-2Y - 7-8Y</p><span class="price">R$ 14,95</span></article>
  <article class="card"><div class="shot" role="img" aria-label="Three pairs of gloves in navy, stripes and teal" style="background:linear-gradient(90deg,#2b3550,#d77a6a,#3fc3c0)"></div><span class="new-tag">NOVO</span><i class="rule"></i><h3 class="name">3 PACK GOVES</h3><p class="size">SIZE: 1½-2Y - 7-8Y</p><s class="old">R$ 8,95</s><span class="sale">R$ 7,95</span></article>
  <article class="card"><div class="shot" role="img" aria-label="Navy polka-dot dress" style="background:#2b3452"></div><i class="rule"></i><h3 class="name">DRESS</h3><p class="size">SIZE: 1½-2Y - 6-8Y</p><span class="price">R$ 4,95</span></article>
  <article class="card"><div class="shot" role="img" aria-label="Dark denim jeans" style="background:#2e3d5c"></div><i class="rule"></i><h3 class="name">JEANS</h3><p class="size">SIZE: 1½-2Y - 6-8Y</p><span class="price">R$ 10,95</span></article>
</main>

<nav class="pager"><span>‹</span><span>1</span><span class="on">2</span><span class="gap">…</span><span>3</span><span>4</span><span>›</span></nav>

<!-- footer -->
<footer>
  <div class="site-footer"></div>
  <h4 class="foot-title" style="left:85px;top:1074px">NAVIGATION</h4>
  <ul class="foot-links" style="left:85px"><li>Home</li><li>Buy</li><li>Sell</li><li>About Us</li></ul>
  <ul class="foot-links" style="left:145px"><li>How it Works</li><li>Privacy Policy</li><li>Terms of Use</li><li>Site Map</li></ul>
  <ul class="foot-links" style="left:222px"><li>FAQ</li><li>Customer Service</li><li>Services</li><li>Support</li></ul>
  <h4 class="foot-title" style="left:347px;top:1077px">CONECT WITH US</h4>
  <div class="socials">
    <span><i style="background:#3b5a98"></i>chatloom</span>
    <span><i style="background:#8a8a8a"></i>quibbly</span>
    <span><i style="background:#6e6e6e"></i>v+</span>
    <span><i style="background:#555"></i>snapquilt</span>
  </div>
  <h4 class="foot-title" style="left:517px;top:1074px">CONTATC US</h4>
  <div class="contact">
    <div><svg width="10" height="9" aria-hidden="true"><path d="M0 3 Q5 -1 10 3 L8 4 L7 2.5 H3 L2 4 Z M2 5 H8 V9 H2 Z" fill="#444"/></svg>0 - 300 418 5520</div>
    <div><svg width="10" height="8" aria-hidden="true"><rect width="10" height="8" fill="#444"/><path d="M0 0 L5 4.5 L10 0" fill="none" stroke="#e6e6e6" stroke-width="1"/></svg>info@mivelda.com</div>
    <address>Rua das Palmeiras Altas 417<br>Sao Paulo-SP, 04518-000<br>BRAZIL</address>
  </div>
  <i class="footer-rule"></i>
  <p class="copyright">© Copyright 2013 - MIVELDA.com - All Rights reserved.</p>
</footer>

</body>
</html>
```